Skyscraper (160x600), Banner (728x90), Banner (300x250)
Zielgruppe
Frauen zwischen 20 und 40 mit Kinderwunsch, die es auf emotionaler Ebene anzusprechen gilt
Aufgabenstellung
Wir suchen ansprechend kreativ gestaltete Werbemittel für unseren Ovulationstest FertiLUNA. Dies ist ein Urin-Schnelltest, mit dem Frauen, die schwanger werden wollen, ihre fruchtbaren Tage bestimmen können. Er funktioniert genauso wie ein Schwangerschaftstest. Die Ansprache soll sehr emotional gestaltet werden, da ein hoch emotionales Thema

```html
<!DOCTYPE html>
<html lang="de">
<head>
<meta charset="utf-8">
<title>FertiLUNA Werbemittel</title>
<link rel="stylesheet" href="https://fonts.googleapis.com/css2?family=Playfair+Display:wght@400;700;900&family=Cinzel:wght@400;700&display=swap">
<style>
:root{
  --bg-top:#cdeef2;
  --bg-bottom:#f7c9b4;
  --panel:#d3d3d3;
  --pink:#f0a8c4;
  --pink-soft:#f7d3e2;
  --blue:#33b8ea;
  --cyan-soft:#bff0f6;
  --ink:#1e1e1e;
  --label:#5b93bb;
  --photo-light:#e9ecef;
  --photo-mid:#aeb6bd;
  --white:#ffffff;
}
*{margin:0;padding:0;box-sizing:border-box}
html,body{width:1200px;height:840px;overflow:hidden}
body{
  position:relative;
  background:linear-gradient(160deg,var(--bg-top) 0%,#f3e6e1 45%,var(--bg-bottom) 100%);
  font-family:"Playfair Display",Georgia,serif;
  color:var(--ink);
}
.abs{position:absolute}
.photo{position:absolute;background:linear-gradient(135deg,var(--photo-light),var(--photo-mid))}
.photo--warm{background:linear-gradient(135deg,#f1e4de,#b9a49a)}
.photo--cool{background:linear-gradient(180deg,#e6f5f7,#9fb3ba)}
.product-box{position:absolute;background:linear-gradient(180deg,#f4f8fb,#cfe2ee);border:1px solid #b8c9d6}
.size-label{position:absolute;font-weight:700;color:var(--label);font-size:30px}
.num{position:absolute;color:var(--label);font-size:17px;font-weight:700}

/* medium rectangle set */
.rect-panel{left:218px;top:15px;width:397px;height:378px;background:var(--panel)}
.rect{position:absolute;width:186px;height:155px;background:var(--pink-soft);overflow:hidden}
.rect .t{position:absolute;line-height:1;text-align:center}

/* skyscraper set */
.sky-panel{left:648px;top:15px;width:534px;height:498px;background:var(--panel)}
.sky{position:absolute;top:24px;width:122px;height:453px;overflow:hidden}
.sky .t{position:absolute;left:0;right:0;text-align:center;line-height:1}
.scene{position:absolute;top:485px;font-size:14px;color:#333;font-family:Georgia,serif}

/* leaderboard set */
.leader{position:absolute;left:38px;width:600px;overflow:hidden;
  background:linear-gradient(90deg,#fbe3ea,var(--pink-soft) 60%,#f6c8d8);
  box-shadow:0 2px 4px rgba(0,0,0,.12)}
.leader .t{position:absolute;font-family:"Cinzel","Playfair Display",serif;white-space:nowrap;line-height:1}
.pk{color:var(--pink)}
.bl{color:var(--blue)}
</style>
</head>
<body>

<!-- 300x250 -->
<div class="abs rect-panel"></div>

<div class="rect" style="left:228px;top:20px">
  <div class="photo" style="left:80px;top:0;width:106px;height:155px" role="img" aria-label="Foto eines Babys"></div>
  <div class="t" style="left:4px;top:28px;width:80px;font-size:40px;font-weight:900">Sie</div>
  <div class="t" style="left:4px;top:74px;width:80px;font-size:15px">wünschen<br>sich ein</div>
  <div class="t bl" style="left:4px;top:108px;width:80px;font-size:24px;font-weight:700">BABY?</div>
</div>
<div class="num" style="left:213px;top:150px">1</div>

<div class="rect" style="left:422px;top:20px">
  <div class="photo photo--warm" style="left:96px;top:0;width:90px;height:155px" role="img" aria-label="Foto einer Mutter mit lachendem Baby"></div>
  <div class="t" style="left:4px;top:8px;width:98px;font-size:22px;font-weight:700">Träumen</div>
  <div class="t" style="left:4px;top:32px;width:98px;font-size:32px;font-weight:900">SIE</div>
  <div class="t" style="left:4px;top:68px;width:98px;font-size:14px">nicht nur von</div>
  <div class="t bl" style="left:4px;top:86px;width:98px;font-size:22px;font-weight:700">IHREM</div>
  <div class="t" style="left:4px;top:112px;width:98px;font-size:22px;font-weight:900">GLÜCK!</div>
</div>
<div class="num" style="left:597px;top:160px">2</div>

<div class="size-label" style="left:350px;top:187px">300x250</div>

<div class="rect" style="left:228px;top:235px">
  <div class="photo photo--warm" style="left:0;top:0;width:92px;height:155px" role="img" aria-label="Foto eines Paares in zärtlicher Umarmung"></div>
  <div class="t" style="left:88px;top:72px;width:96px;font-size:11px">Bestimmen</div>
  <div class="t" style="left:88px;top:84px;width:96px;font-size:16px;font-weight:900">SIE <span style="font-size:10px;font-weight:400">den</span></div>
  <div class="t" style="left:88px;top:102px;width:96px;font-size:10px">idealen Zeitpunkt</div>
  <div class="t" style="left:88px;top:116px;width:96px;font-size:9px">zum schwanger</div>
  <div class="t" style="left:88px;top:128px;width:96px;font-size:10px">werden mit <b>FertiLUNA</b></div>
</div>
<div class="num" style="left:213px;top:375px">3</div>

<div class="rect" style="left:422px;top:235px;background:var(--white)">
  <div class="photo photo--warm" style="left:110px;top:0;width:76px;height:155px" role="img" aria-label="Foto eines Babybauchs"></div>
  <div class="t" style="left:6px;top:10px;width:104px;font-size:22px;font-weight:700">und</div>
  <div class="t" style="left:6px;top:32px;width:104px;font-size:11px">ein grosser</div>
  <div class="t" style="left:6px;top:44px;width:104px;font-size:14px;font-weight:700">WUNSCH</div>
  <div class="t bl" style="left:6px;top:60px;width:104px;font-size:18px;font-weight:700">kann</div>
  <div class="t" style="left:6px;top:78px;width:104px;font-size:18px;font-weight:700">wahr</div>
  <div class="t" style="left:6px;top:96px;width:104px;font-size:18px;font-weight:700">werden!</div>
  <div class="product-box" style="left:8px;top:122px;width:80px;height:26px" role="img" aria-label="Verpackung des FertiLUNA Ovulationstests"></div>
</div>
<div class="num" style="left:598px;top:377px">4</div>

<!-- 160x600 -->
<div class="abs sky-panel"></div>

<div class="sky" style="left:668px;background:var(--cyan-soft)">
  <div class="photo photo--cool" style="left:0;top:0;width:122px;height:250px" role="img" aria-label="Foto eines Babys"></div>
  <div class="t" style="top:262px;font-size:42px;font-weight:900">Sie</div>
  <div class="t" style="top:306px;font-size:19px">wünschen</div>
  <div class="t" style="top:330px;font-size:19px">sich ein</div>
  <div class="t bl" style="top:356px;font-size:30px;font-weight:700;color:#7ccbe0">BABY?</div>
</div>
<div class="scene" style="left:668px">Szene1</div>

<div class="sky" style="left:795px;background:var(--white)">
  <div class="photo" style="left:0;top:0;width:122px;height:320px" role="img" aria-label="Foto einer Mutter mit lachendem Baby"></div>
  <div class="t" style="top:290px;font-size:24px;font-weight:700">Träumen</div>
  <div class="t" style="top:318px;font-size:44px;font-weight:900">SIE</div>
  <div class="t" style="top:366px;font-size:16px">nicht nur von</div>
  <div class="t" style="top:386px;font-size:30px;font-weight:700;color:#999">IHREM</div>
  <div class="t" style="top:422px;font-size:16px;font-weight:700;color:#999">BABYGLÜCK!</div>
</div>
<div class="scene" style="left:795px">Szene2</div>

<div class="sky" style="left:923px;background:var(--cyan-soft)">
  <div class="photo photo--cool" style="left:0;top:300px;width:122px;height:153px" role="img" aria-label="Foto eines Paares in zärtlicher Umarmung"></div>
  <div class="t" style="top:18px;font-size:20px;font-weight:700">Bestimmen</div>
  <div class="t" style="top:42px;font-size:44px;font-weight:900">SIE</div>
  <div class="t" style="top:90px;font-size:16px">den idealen</div>
  <div class="t bl" style="top:110px;font-size:16px;color:#fff;letter-spacing:1px">ZEITPUNKT</div>
  <div class="t" style="top:130px;font-size:30px;font-weight:900">zum</div>
  <div class="t" style="top:164px;font-size:18px">schwanger</div>
  <div class="t" style="top:186px;font-size:30px;font-weight:900">werden</div>
  <div class="t" style="top:220px;font-size:18px;font-weight:700">mit</div>
  <div class="t" style="top:244px;font-size:20px;font-weight:700;color:#7a9aa6">FertiLUNA</div>
</div>
<div class="scene" style="left:923px">Szene3</div>

<div class="sky" style="left:1050px;background:var(--white)">
  <div class="photo photo--warm" style="left:30px;top:210px;width:92px;height:150px" role="img" aria-label="Foto eines Babybauchs"></div>
  <div class="t" style="top:14px;font-size:30px;font-weight:700;color:var(--pink)">und</div>
  <div class="t" style="top:46px;font-size:14px;color:var(--pink)">ein grosser</div>
  <div class="t" style="top:62px;font-size:20px;font-weight:700;color:var(--pink)">WUNSCH</div>
  <div class="t bl" style="top:86px;font-size:26px;font-weight:700;color:#6fa7c9">kann</div>
  <div class="t" style="top:116px;font-size:26px;font-weight:700;color:#6fa7c9">wahr</div>
  <div class="t" style="top:146px;font-size:26px;font-weight:700;color:var(--pink)">werden!</div>
  <div class="product-box" style="left:6px;top:370px;width:96px;height:54px" role="img" aria-label="Verpackung des FertiLUNA Ovulationstests"></div>
</div>
<div class="scene" style="left:1050px">Szene4</div>

<div class="size-label" style="left:1050px;top:518px">160x600</div>

<!-- 728x90 -->
<div class="size-label" style="left:37px;top:405px">728x90</div>

<div class="num" style="left:16px;top:505px">1.</div>
<div class="leader" style="top:450px;height:75px">
  <div class="photo" style="left:0;top:0;width:118px;height:75px" role="img" aria-label="Foto eines Babys"></div>
  <div class="t" style="left:120px;top:20px;font-size:36px;font-weight:700"><span class="pk">Sie</span> <span style="font-size:24px;color:#6b8fa8">wünschen sich ein</span> <span class="pk">Baby?</span></div>
</div>

<div class="num" style="left:16px;top:595px">2.</div>
<div class="leader" style="top:545px;height:70px">
  <div class="photo photo--warm" style="left:534px;top:0;width:66px;height:70px" role="img" aria-label="Foto einer Mutter mit Baby"></div>
  <div class="t pk" style="left:16px;top:10px;font-size:20px;font-weight:700">Träumen</div>
  <div class="t" style="left:16px;top:33px;font-size:27px;color:#6b8fa8">Sie nicht nur von Ihrem <span class="pk" style="font-size:36px;font-weight:700">Glück!</span></div>
</div>

<div class="num" style="left:16px;top:688px">3.</div>
<div class="leader" style="top:635px;height:73px">
  <div class="photo photo--warm" style="left:0;top:0;width:150px;height:73px" role="img" aria-label="Foto eines Paares in zärtlicher Umarmung"></div>
  <div class="t pk" style="left:152px;top:12px;font-size:19px;font-weight:700">Bestimmen Sie den idealen Zeitpunkt</div>
  <div class="t" style="left:152px;top:40px;font-size:19px;color:#6b8fa8">zum schwanger werden mit <span class="pk" style="font-weight:700">FertiLUNA</span></div>
</div>

<div class="num" style="left:16px;top:778px">4.</div>
<div class="leader" style="top:726px;height:74px;background:var(--white)">
  <div class="product-box" style="left:8px;top:14px;width:110px;height:44px" role="img" aria-label="Verpackung des FertiLUNA Ovulationstests"></div>
  <div class="photo photo--warm" style="left:520px;top:0;width:80px;height:74px" role="img" aria-label="Foto eines Babybauchs"></div>
  <div class="t pk" style="left:130px;top:10px;font-size:20px">... und ein grosser</div>
  <div class="t" style="left:150px;top:34px;font-size:30px;color:#6b8fa8">Wunsch<span class="pk" style="font-size:20px"> kann wahr </span>werden!</div>
</div>

</body>
</html>
```